Law Firm Stationery Design - Traditional Meets Intuitive

Looking for a modern, yet classic, law firm stationery design. Simplicity is desired, but great ideas are encouraged. See attachment for company information. We utilize a variety of non-traditional legal tools to bring a different perspective to each of our client's particular situation. Final design should communicate classic values with intuitive, unique solutions.

Industry/Entity Type

Law Firm

Requirements
Should not have
• - No typical legal icons
• - No Tag Line!
• - DO NOT WANT WHAT WE ALREADY HAVE

```html
<!DOCTYPE html>
<html lang="en">
<head>
<meta charset="utf-8">
<title>Veridane Law LLC – Stationery</title>
<link rel="stylesheet" href="https://fonts.googleapis.com/css2?family=Tinos:wght@400;700&family=Open+Sans:wght@400;600&display=swap">
<style>
  :root {
    --bg: #e4e4e4;
    --paper: #ffffff;
    --taupe: #8c7468;
    --ink: #111111;
    --text: #222222;
    --flap: #f1f1f1;
    --shadow: rgba(0,0,0,.18);
  }
  * { box-sizing: border-box; margin: 0; padding: 0; }
  html, body { width: 1200px; height: 2571px; overflow: hidden; }
  body { background: var(--bg); font-family: "Tinos", "Times New Roman", serif; color: var(--text); position: relative; }

  .sheet { position: absolute; background: var(--paper); box-shadow: 0 4px 14px var(--shadow); overflow: hidden; }
  .edge-band { position: absolute; left: 0; top: 0; bottom: 0; width: 1.3%; background: var(--taupe); }
  .edge-band::after { content: ""; position: absolute; left: 0; right: 0; bottom: 0; height: 28%; background: var(--ink); }
  .corner { position: absolute; top: 0; right: 0; }
  .corner path { fill: var(--ink); }

  .logo { display: inline-flex; flex-direction: column; align-items: center; font-family: "Tinos", serif; font-weight: 400; color: var(--taupe); line-height: 1; }
  .logo-name { letter-spacing: .02em; }
  .logo-sub { letter-spacing: .04em; margin-top: .12em; }

  /* Letterhead */
  .letterhead { left: 60px; top: 70px; width: 700px; height: 990px; }
  .letterhead .corner { width: 120px; height: 150px; }
  .letterhead .logo { position: absolute; left: 50px; top: 50px; }
  .letterhead .logo-name { font-size: 42px; }
  .letterhead .logo-sub { font-size: 26px; }
  .letter-body { position: absolute; left: 50px; right: 60px; top: 230px; font-size: 15.5px; line-height: 1.32; }
  .letter-body p { margin-bottom: 15px; }
  .letter-footer { position: absolute; left: 50px; bottom: 34px; font-family: "Open Sans", sans-serif; font-size: 11px; line-height: 1.45; color: var(--text); }
  .letter-footer .firm { color: var(--taupe); font-weight: 600; }

  /* Business cards */
  .card-front { left: 830px; top: 110px; width: 310px; height: 177px; display: flex; align-items: center; justify-content: center; }
  .card-front .logo-name { font-size: 30px; }
  .card-front .logo-sub { font-size: 19px; }

  .card-back-small { left: 830px; top: 320px; width: 310px; height: 177px; }
  .card-back-small .corner { width: 70px; height: 80px; }
  .card-back-small .logo { position: absolute; right: 40px; top: 18px; }
  .card-back-small .logo-name { font-size: 20px; }
  .card-back-small .logo-sub { font-size: 13px; }
  .card-back-small .person { position: absolute; left: 22px; top: 22px; font-family: "Open Sans", sans-serif; color: var(--taupe); font-size: 12px; font-weight: 600; }
  .card-back-small .person small { display: block; font-size: 9px; font-weight: 400; color: var(--text); }
  .card-back-small .details { position: absolute; left: 22px; bottom: 16px; font-family: "Open Sans", sans-serif; font-size: 8.5px; line-height: 1.45; }

  /* DL envelope, back */
  .envelope-back { left: 830px; top: 530px; width: 310px; height: 160px; display: flex; flex-direction: column; align-items: center; }
  .envelope-back .flap { position: absolute; left: 0; top: 0; width: 100%; height: 52px; }
  .envelope-back .flap path { fill: var(--flap); stroke: #d6d6d6; stroke-width: 1; }
  .envelope-back .logo { margin-top: 30px; position: relative; }
  .envelope-back .logo-name { font-size: 22px; }
  .envelope-back .logo-sub { font-size: 14px; }
  .envelope-back .web { position: absolute; bottom: 22px; font-family: "Open Sans", sans-serif; font-size: 10px; letter-spacing: .12em; }

  /* Small envelope, front */
  .envelope-small { left: 830px; top: 725px; width: 310px; height: 180px; }
  .envelope-small .corner { width: 60px; height: 72px; }
  .envelope-small .logo { position: absolute; left: 16px; top: 18px; }
  .envelope-small .logo-name { font-size: 22px; }
  .envelope-small .logo-sub { font-size: 14px; }
  .envelope-small .return { position: absolute; left: 16px; bottom: 14px; font-family: "Open Sans", sans-serif; font-size: 8px; line-height: 1.4; }

  /* Large envelope, front */
  .envelope-large { left: 60px; top: 1120px; width: 1080px; height: 600px; }
  .envelope-large .corner { width: 170px; height: 200px; }
  .envelope-large .logo { position: absolute; left: 60px; top: 60px; }
  .envelope-large .logo-name { font-size: 64px; }
  .envelope-large .logo-sub { font-size: 38px; }
  .envelope-large .return { position: absolute; left: 60px; bottom: 50px; font-family: "Open Sans", sans-serif; font-size: 17px; line-height: 1.45; }

  /* Large business card, back */
  .card-back { left: 60px; top: 1810px; width: 1080px; height: 617px; }
  .card-back .edge-band { width: 2%; }
  .card-back .corner { width: 190px; height: 220px; }
  .card-back .logo { position: absolute; right: 230px; top: 70px; }
  .card-back .logo-name { font-size: 72px; }
  .card-back .logo-sub { font-size: 42px; }
  .card-back .person { position: absolute; left: 80px; top: 90px; font-family: "Open Sans", sans-serif; }
  .card-back .person-name { font-size: 44px; font-weight: 600; color: var(--taupe); }
  .card-back .person-role { font-size: 28px; color: var(--text); margin-top: 2px; }
  .card-back .details { position: absolute; left: 80px; bottom: 70px; font-family: "Open Sans", sans-serif; font-size: 30px; line-height: 1.35; }
  .details .firm { color: var(--taupe); font-weight: 600; }
  .detail-row { display: flex; align-items: center; gap: .35em; }
  .detail-row.indent { padding-left: .75em; }
  .icon { width: .55em; height: .55em; flex: none; fill: var(--taupe); }
</style>
</head>
<body>

  <!-- Letterhead -->
  <section class="sheet letterhead" aria-label="Letterhead">
    <span class="edge-band"></span>
    <svg class="corner" viewBox="0 0 100 100" preserveAspectRatio="none" aria-hidden="true"><path d="M20 0 H100 V100 C100 40 75 0 20 0 Z"/></svg>
    <div class="logo"><span class="logo-name">VERIDANE</span><span class="logo-sub">LAW LLC</span></div>
    <div class="letter-body">
      <p>Dear Ms. Harlow:</p>
      <p>Nothing is as exciting as getting ready for game day.</p>
      <p>The players warming up, the buzz of the crowd as they enter the park, even the smell of the stadium, all make for an electrically charged atmosphere. I’ve seen it first hand, and I love it.</p>
      <p>I’ve been around professional sports since I was a child. My father worked as a Premier Circuit Baseball scout for more than 35 years. Even more importantly, I had the pleasure of spending this past summer as an intern for the Ridgeport Riveters minor league baseball team.</p>
      <p>It was an amazing experience. I interned in the Public/Media Relations department and had a chance to try my hand at an incredible variety of projects. I worked with FieldCast as they covered the play of Tom Reyes Jr. and a Hawks/Rams Legends game. I handled all our player appearances. I even set up and ran our first baseball camp. I usually put in 80 hours a week and couldn’t get enough!</p>
      <p>The Riveter experience, in addition to work for the Lakeport Bears and my Sports Management major, all have me extremely interested in pursuing a career as an Sports Marketing upon graduation.</p>
      <p>I would love to talk with you more about my passion, my background, and your organization. I look forward to touching base with you soon.</p>
      <p>Regards,</p>
      <p>Nora Quill</p>
    </div>
    <div class="letter-footer">
      <div class="firm">VERIDANE LAW LLC</div>
      <div>18 Harbor Lane, Suite 300</div>
      <div>Easton, MA 02375</div>
      <div>Phone: 617-555-0148</div>
      <div>www.veridanelaw.com</div>
    </div>
  </section>

  <!-- Business card, front -->
  <section class="sheet card-front" aria-label="Business card front">
    <div class="logo"><span class="logo-name">VERIDANE</span><span class="logo-sub">LAW LLC</span></div>
  </section>

  <!-- Business card, back (small) -->
  <section class="sheet card-back-small" aria-label="Business card back">
    <span class="edge-band"></span>
    <svg class="corner" viewBox="0 0 100 100" preserveAspectRatio="none" aria-hidden="true"><path d="M20 0 H100 V100 C100 40 75 0 20 0 Z"/></svg>
    <div class="person">Daniel Marsh<small>President</small></div>
    <div class="logo"><span class="logo-name">VERIDANE</span><span class="logo-sub">LAW LLC</span></div>
    <div class="details">
      <div class="firm">VERIDANE LAW LLC</div>
      <div>18 Harbor Lane, Suite 300</div>
      <div>Easton, MA 02375</div>
      <div>Phone: 617-555-0148</div>
      <div>www.veridanelaw.com</div>
    </div>
  </section>

  <!-- DL envelope, back -->
  <section class="sheet envelope-back" aria-label="Envelope back">
    <svg class="flap" viewBox="0 0 100 52" preserveAspectRatio="none" aria-hidden="true"><path d="M0 0 L8 40 Q10 50 18 50 H82 Q90 50 92 40 L100 0 Z"/></svg>
    <div class="logo"><span class="logo-name">VERIDANE</span><span class="logo-sub">LAW LLC</span></div>
    <div class="web">www.veridanelaw.com</div>
  </section>

  <!-- Small envelope, front -->
  <section class="sheet envelope-small" aria-label="Small envelope front">
    <span class="edge-band"></span>
    <svg class="corner" viewBox="0 0 100 100" preserveAspectRatio="none" aria-hidden="true"><path d="M20 0 H100 V100 C100 40 75 0 20 0 Z"/></svg>
    <div class="logo"><span class="logo-name">VERIDANE</span><span class="logo-sub">LAW LLC</span></div>
    <div class="return">If undelivered, please return to:<br>18 Harbor Lane, Suite 300 Easton, MA 02375</div>
  </section>

  <!-- Large envelope, front -->
  <section class="sheet envelope-large" aria-label="Large envelope front">
    <span class="edge-band"></span>
    <svg class="corner" viewBox="0 0 100 100" preserveAspectRatio="none" aria-hidden="true"><path d="M20 0 H100 V100 C100 40 75 0 20 0 Z"/></svg>
    <div class="logo"><span class="logo-name">VERIDANE</span><span class="logo-sub">LAW LLC</span></div>
    <div class="return">If undelivered, please return to:<br>18 Harbor Lane, Suite 300 Easton, MA 02375</div>
  </section>

  <!-- Business card, back (large) -->
  <section class="sheet card-back" aria-label="Business card back, detail">
    <span class="edge-band"></span>
    <svg class="corner" viewBox="0 0 100 100" preserveAspectRatio="none" aria-hidden="true"><path d="M20 0 H100 V100 C100 40 75 0 20 0 Z"/></svg>
    <div class="person">
      <div class="person-name">Daniel Marsh</div>
      <div class="person-role">President</div>
    </div>
    <div class="logo"><span class="logo-name">VERIDANE</span><span class="logo-sub">LAW LLC</span></div>
    <div class="details">
      <div class="firm">VERIDANE LAW LLC</div>
      <div class="detail-row">
        <svg class="icon" viewBox="0 0 10 10" aria-hidden="true"><path d="M5 0 A3.5 3.5 0 0 1 8.5 3.5 C8.5 6 5 10 5 10 C5 10 1.5 6 1.5 3.5 A3.5 3.5 0 0 1 5 0 Z M5 2 A1.5 1.5 0 1 0 5 5 A1.5 1.5 0 1 0 5 2 Z"/></svg>
        18 Harbor Lane, Suite 300
      </div>
      <div class="detail-row indent">Easton, MA 02375</div>
      <div class="detail-row">
        <svg class="icon" viewBox="0 0 10 10" aria-hidden="true"><path d="M2 0.5 L4 0.5 L4.8 3 L3.5 4 Q4.5 6 6 6.5 L7 5.2 L9.5 6 L9.5 8 Q9.5 9.5 8 9.5 Q1 9 0.5 2 Q0.5 0.5 2 0.5 Z"/></svg>
        Phone: 617-555-0148
      </div>
      <div class="detail-row">
        <svg class="icon" viewBox="0 0 10 10" aria-hidden="true"><circle cx="5" cy="5" r="4.5"/></svg>
        www.veridanelaw.com
      </div>
    </div>
  </section>

</body>
</html>
```